Web re-design project www.vempresoft.com

We need a corporate website for a startup company called Vempre Labs. The company offers web-based worksite management system for big construction companies. In short, replacing annoying papers with iPads.
We need the site main page to provide basic overview of the company and then inner page layout for displaying news and detailed information about products.
Currently we have a site up at:
http://www.vempresoft.com/en/main
but as you can see the graphic design is a bit lacking in quality(implemented by a tech guy :)
We need you to pimp that web site design up!
There is possibility for more freelance work in the future related to our web products, slide show designs and printed marketing materials.
Our main product is LOMVI. You can find a short presentation about what it does here:
http://www.vempresoft.com/en/lomvi
Here you can find packages of images and screenshots related to our company:
https://files.plimbox.net/u/7719026/vempre_images.zip
https://files.plimbox.net/u/7719026/vempresoft%20images2.zip
Product logo svg can be found here:
https://files.plimbox.net/u/7719026/LOMVI-logo.svg
Your are not forced to use those images, but hopefully there will be something that is useful.
Hope to hear from you guys soon!
Cheers,
Ossi
Update:
We will be using LOMVI logo as the company brand. I don't like our current Vempre Labs company logo, so that doesn't need to be included in the site design.
Update 2:
I like website designs that are "light", elegant and pretty simplistic. One example is our product login page (screenshot included in files).
Update 3:
Sites from the same industry / type of products:
http://www.rakmoda.fi/
http://www.quarvelgrid.com/products/software/network-applications/fieldsync-3d
http://www.dornvex.com/construction/heavy-civil/software-solutions/Linked-Network.aspx?dtID=overview&
Target audience for the website is companies in the construction sector, and possibly corporate investors
Graphic Design

```html
<!DOCTYPE html>
<html lang="en">
<head>
<meta charset="utf-8">
<title>LOMVI – Worksite Data Management</title>
<link rel="stylesheet" href="https://fonts.googleapis.com/css2?family=Ubuntu:ital,wght@0,300;0,400;0,500;1,300;1,400&display=swap">
<style>
  :root{
    --red:#e3101b;
    --red-dark:#c4000c;
    --red-light:#ea2a33;
    --white:#ffffff;
    --ink:#222222;
    --text:#6f6f6f;
    --muted:#8c8c8c;
    --rule:#d6d6d6;
    --footer:#ececec;
  }
  *{margin:0;padding:0;box-sizing:border-box}
  html,body{width:1200px;height:880px;overflow:hidden;background:var(--white)}
  body{position:relative;font-family:"Ubuntu",sans-serif;color:var(--text)}
  a{color:inherit;text-decoration:none}

  .site-header{position:absolute;left:0;top:0;width:1200px;height:80px;background:var(--white)}
  .brand{position:absolute;left:224px;top:20px;display:flex;align-items:center;gap:12px;
    font-size:30px;font-weight:400;color:var(--ink);letter-spacing:.5px;line-height:36px}
  .brand-dot{width:30px;height:30px;border-radius:50%;background:var(--ink)}
  .main-nav{position:absolute;left:712px;top:26px;width:280px;height:31px;border-bottom:1px solid var(--rule)}
  .main-nav a{position:absolute;top:0;font-size:13px;font-weight:300;color:#666}
  .main-nav a.is-active{color:var(--red)}

  .hero{position:absolute;left:0;top:80px;width:1200px;height:368px;
    background:linear-gradient(180deg,var(--red-dark) 0%,var(--red-light) 100%)}
  .hero-slide{position:absolute;left:192px;top:22px;width:816px;height:320px;overflow:hidden;
    background:linear-gradient(100deg,#6d6a5f 0%,#8d8478 35%,#9a8f83 60%,#7e7468 100%);
    box-shadow:0 4px 8px rgba(0,0,0,.25)}
  .hero-photo{position:absolute;inset:0}
  .hero-caption{position:absolute;left:0;top:113px;width:530px;height:97px;background:rgba(30,30,30,.6);
    padding:16px 0 0 78px;color:var(--white)}
  .hero-caption h1{font-size:38px;font-weight:300;line-height:40px;letter-spacing:.5px}
  .hero-caption p{font-size:19px;font-weight:300;line-height:26px;color:#e6e6e6}
  .hero-arrow{position:absolute;top:140px}
  .hero-arrow.prev{left:24px}
  .hero-arrow.next{left:1134px}

  .intro-title{position:absolute;left:223px;top:477px;font-size:15px;font-weight:400;color:var(--red)}
  .intro-rule{position:absolute;left:0;top:504px;width:1200px;height:1px;background:var(--rule)}
  .intro-rule-accent{position:absolute;left:192px;top:503px;width:816px;height:2px;background:var(--red)}
  .tagline{position:absolute;left:0;top:531px;width:1200px;text-align:center;font-size:18px;
    font-style:italic;font-weight:300;color:var(--muted)}
  .tagline-rule{position:absolute;left:208px;top:569px;width:784px;height:1px;background:#e2e2e2}

  .intro-col{position:absolute;top:590px;width:356px;font-size:10px;line-height:11.7px;color:var(--text)}
  .intro-col p+p{margin-top:11.7px}
  .intro-col.left{left:223px}
  .intro-col.right{left:622px}
  .intro-col a{color:var(--red);font-style:italic;font-weight:500;text-decoration:underline}

  .site-footer{position:absolute;left:0;top:760px;width:1200px;height:120px;background:var(--footer);
    font-size:10px;color:var(--muted)}
  .footer-meta{position:absolute;left:223px;top:24px}
  .footer-meta .accent{color:var(--red)}
  .footer-meta a.mail{color:var(--red);text-decoration:underline}
  .footer-meta .sep{margin:0 6px}
  .footer-social{position:absolute;left:780px;top:23px;display:flex;align-items:center}
  .footer-social span{margin-right:6px}
  .social-link{width:13px;height:13px;margin-right:3px;background:#9a9a9a;border-radius:2px;display:inline-block}
</style>
</head>
<body>
  <header class="site-header">
    <a class="brand" href="#"><span class="brand-dot"></span>LOMVI</a>
    <nav class="main-nav">
      <a class="is-active" href="#" style="left:19px">Home</a>
      <a href="#" style="left:85px">Products</a>
      <a href="#" style="left:166px">News</a>
      <a href="#" style="left:222px">Contact</a>
    </nav>
  </header>

  <section class="hero">
    <svg class="hero-arrow prev" width="42" height="82" viewBox="0 0 42 82" aria-label="Previous slide">
      <path d="M40 2 L4 41 L40 80" fill="none" stroke="rgba(255,255,255,.55)" stroke-width="2"/>
      <path d="M34 2 L2 41 L34 80" fill="none" stroke="rgba(255,255,255,.35)" stroke-width="1"/>
    </svg>
    <div class="hero-slide">
      <div class="hero-photo" role="img" aria-label="Site engineer in a hi-vis vest using a tablet on a gravel road worksite, with tablet and phone showing the LOMVI map app"></div>
      <div class="hero-caption">
        <h1>LOMVI</h1>
        <p>WEB based Worksite Data Management service</p>
      </div>
    </div>
    <svg class="hero-arrow next" width="42" height="82" viewBox="0 0 42 82" aria-label="Next slide">
      <path d="M2 2 L38 41 L2 80" fill="none" stroke="rgba(255,255,255,.55)" stroke-width="2"/>
      <path d="M8 2 L40 41 L8 80" fill="none" stroke="rgba(255,255,255,.35)" stroke-width="1"/>
    </svg>
  </section>

  <h2 class="intro-title">Welcome on our site!</h2>
  <div class="intro-rule"></div>
  <div class="intro-rule-accent"></div>
  <p class="tagline">Lomvi is a cloud-based service for road construction projects and it’s going full steam!</p>
  <div class="tagline-rule"></div>

  <div class="intro-col left">
    <p>Donec vel risus eu quam iaculis luctus. Phasellus et leo sed nibh scelerisque varius non vitae diam. Curabitur pulvinar faucibus urna et gravida. Donec vitae justo at enim feugiat faucibus vitae eu urna. Praesent odio massa, eleifend id ultricies at, ultricies vitae tortor. Aenean dapibus iaculis erat id pretium. Suspendisse vitae magna odio, <a href="#">eget vestibulum urna</a>. Cum sociis natoque penatibus et magnis dis parturient montes, nascetur ridiculus mus.</p>
    <p>Massa, fermentum ac gravida sed, feugiat quis felis. In nisl ligula, luctus in sagittis et, venenatis ut felis. Nulla ut rhoncus sapien. Phasellus tempus elementum eros, ut vestibulum felis cursus vel.</p>
  </div>
  <div class="intro-col right">
    <p>Nam in arcu arcu, eget dignissim nisl. Sed tincidunt, justo eget faucibus molestie, nibh turpis lobortis lorem, et malesuada lacus augue eget nibh. Etiam id tortor id purus molestie vestibulum nec eu massa. Nam blandit velit quis urna vulputate malesuada. Praesent venenatis nunc at nulla volutpat faucibus. Nunc purus massa, fermentum ac gravida sed, feugiat quis felis. In nisl ligula, luctus in sagittis et, venenatis ut felis. Nulla ut rhoncus sapien. Phasellus tempus elementum eros, ut vestibulum felis cursus vel. Suspendisse vitae ipsum sit amet ipsum feugiat sodales.</p>
  </div>

  <footer class="site-footer">
    <div class="footer-meta">Copyright © 2012 <span class="accent">Vempre Labs</span><span class="sep">|</span>www.vempresoft.com<span class="sep">|</span><a class="mail" href="#">info@vempresoft.com</a></div>
    <div class="footer-social">
      <span>Follow us on social media:</span>
      <a class="social-link" href="#" aria-label="Social network 1"></a>
      <a class="social-link" href="#" aria-label="Social network 2"></a>
      <a class="social-link" href="#" aria-label="News feed"></a>
      <a class="social-link" href="#" aria-label="Social network 3"></a>
      <a class="social-link" href="#" aria-label="Social network 4"></a>
    </div>
  </footer>
</body>
</html>
```